La Brisa Taqueria

We need layouts for the attached 6 pages. The elements that are within the PDF are to be included in the design but their placement, the colors, everything that is there is completely up to your design ability so please get creative.
We like clean, web 2.0 type designs. Here is a restaurant with a nice design:http://cocinaverdefalls.com/ It does not need to be like this at all, just for a concept of what we like.
The logo on the top left of the site is our logo. I've attached it and a PDF containing the elements of the site here.

```html
<!DOCTYPE html>
<html lang="en">
<head>
<meta charset="utf-8">
<title>La Brisa Taqueria – Gallery</title>
<link rel="stylesheet" href="https://fonts.googleapis.com/css2?family=Roboto+Condensed:wght@400;700&family=Arimo:wght@400&family=Great+Vibes&family=Oswald:wght@500&display=swap">
<style>
:root{
  --gold:#c9952b;
  --gold-dark:#6b4a0c;
  --gold-mid:#8a6314;
  --ink:#000;
  --panel:rgba(0,0,0,.82);
  --text:#fff;
  --muted:#8a8a8a;
}
*{margin:0;padding:0;box-sizing:border-box}
html,body{width:1200px;height:923px;overflow:hidden;background:#1a1410}
body{position:relative;font-family:'Arimo',Arial,sans-serif;color:var(--text)}
.backdrop{position:absolute;inset:0;background:
  radial-gradient(ellipse at 15% 70%,#4a4440 0%,transparent 45%),
  radial-gradient(ellipse at 90% 55%,#6b4e1e 0%,transparent 45%),
  radial-gradient(ellipse at 50% 10%,#3a2a20 0%,transparent 50%),
  linear-gradient(180deg,#1d1512,#2a201a 60%,#141110)}
.abs{position:absolute}
.brand{left:171px;top:60px;display:flex;align-items:center;gap:10px}
.brand-mark{width:16px;height:16px;background:var(--gold)}
.brand-name{font-family:'Roboto Condensed',sans-serif;font-weight:700;font-size:22px;color:var(--gold);letter-spacing:.5px}
.brand-tag{left:197px;top:92px;font-size:12px;letter-spacing:2px;color:#eee;font-family:'Arimo',sans-serif}
.social{left:904px;top:74px;display:flex;gap:6px}
.social span{width:26px;height:26px;border:2px solid var(--gold);border-radius:50%}
.nav{left:0;top:122px;width:1200px;font-family:'Roboto Condensed',sans-serif;font-size:14.5px;text-transform:uppercase}
.nav a{position:absolute;color:#fff;text-decoration:none}
.nav a.active{color:var(--gold)}
.frame{left:171px;top:163px;width:858px;height:674px;background:rgba(0,0,0,.6)}
.reserve{left:184px;top:177px;width:198px;height:296px;background:var(--ink)}
.reserve-title{left:198px;top:189px;width:172px;height:82px;border:1px solid #555;text-align:center}
.reserve-title b{display:block;font-family:'Oswald',sans-serif;font-weight:500;font-size:28px;color:var(--gold);line-height:1;margin-top:10px}
.reserve-title i{display:block;font-family:'Great Vibes',cursive;font-style:normal;font-size:34px;line-height:.9;color:#fff}
.form{left:198px;top:288px;width:172px;height:172px;border:1px solid var(--gold-dark)}
.field{position:absolute;left:14px;width:142px;height:24px;border:1px solid var(--gold-dark);font-size:8px;color:#bbb;padding:7px 10px}
.find{position:absolute;left:14px;top:117px;width:142px;height:33px;background:var(--gold-dark);padding:3px}
.find span{display:block;height:100%;border:1px solid var(--gold);font-family:'Roboto Condensed',sans-serif;font-size:15px;text-align:center;line-height:25px}
.special{left:184px;top:485px;width:198px;height:339px;background:linear-gradient(180deg,#6a4a0b 0%,#6a4a0b 58%,#4a3010 75%,#6b3c25 100%)}
.special-inner{position:absolute;inset:8px;border:1px solid rgba(255,220,150,.55);text-align:center}
.special-photo{position:absolute;left:0;right:0;bottom:0;height:145px;background:linear-gradient(180deg,rgba(60,35,15,0),#5a3524 40%,#7a5a3a)}
.special h2{font-family:'Great Vibes',cursive;font-weight:400;font-size:44px;line-height:.78;margin-top:22px}
.special p{font-size:10.5px;line-height:19px;margin-top:10px}
.more{display:inline-block;margin-top:8px;width:136px;height:28px;border:1px solid #e8d6a8;font-family:'Roboto Condensed',sans-serif;font-size:14px;line-height:26px;position:relative;z-index:1}
.gallery{left:398px;top:175px;width:618px;height:651px;background:var(--ink)}
.gallery h1{position:absolute;left:28px;top:14px;font-family:'Great Vibes',cursive;font-weight:400;font-size:50px;color:var(--gold)}
.rule{position:absolute;left:21px;top:97px;width:577px;height:1px;background:var(--gold-dark)}
.intro{position:absolute;left:29px;top:117px;width:570px;font-size:13px;line-height:27px;color:var(--muted)}
.tile{position:absolute;width:181px;height:181px;overflow:hidden}
.tile .photo{position:absolute;inset:0}
.tile .caption{position:absolute;left:0;right:0;bottom:0;height:35px;background:rgba(60,60,60,.75);font-family:'Roboto Condensed',sans-serif;font-size:11.5px;line-height:35px;padding-left:13px;text-transform:uppercase}
.pager{position:absolute;left:544px;top:604px;display:flex;gap:1px}
.pager span{width:27px;height:27px;background:var(--gold-mid);display:flex;align-items:center;justify-content:center}
.footer{left:177px;top:857px;font-size:11px;color:#fff;word-spacing:0}
.footer .sep{margin:0 16px}
.copy{left:810px;top:857px;width:210px;text-align:right;font-size:11px}
</style>
</head>
<body>
<div class="backdrop" role="img" aria-label="Dimmed restaurant food photograph with stone bowl and tortilla chips"></div>

<div class="abs brand"><span class="brand-mark"></span><span class="brand-name">La Brisa Taqueria</span></div>
<div class="abs brand-tag">Restaurant &amp; Bar</div>

<div class="abs social" aria-label="Social links"><span></span><span></span><span></span><span></span></div>

<nav class="abs nav">
  <a style="left:493px" href="#">Home</a>
  <a style="left:580px" href="#">Menu</a>
  <a style="left:668px" href="#">Contact</a>
  <a style="left:773px" href="#">Calender</a>
  <a style="left:885px" href="#">Press</a>
  <a style="left:976px" class="active" href="#">Gallery</a>
</nav>

<div class="abs frame"></div>

<div class="abs reserve"></div>
<div class="abs reserve-title"><b>Make a</b><i>Reservation</i></div>
<div class="abs form">
  <div class="field" style="top:14px">DATE :</div>
  <div class="field" style="top:50px">TIME :</div>
  <div class="field" style="top:84px">MEMBERS :</div>
  <div class="find"><span>FIND A TABLE</span></div>
</div>

<div class="abs special">
  <div class="special-photo" role="img" aria-label="Photo of grilled lamb chops on greens"></div>
  <div class="special-inner">
    <h2>Weekend<br>&nbsp;&nbsp;Special</h2>
    <p>It is a long established fact that<br>a reader will be distracted...</p>
    <span class="more">CLICK FOR MORE</span>
  </div>
</div>

<section class="abs gallery">
  <h1>Photo Gallery</h1>
  <div class="rule"></div>
  <p class="intro">Lorem Ipsum is simply dummy text of the printing and typesetting industry. Lorem Ipsum has been the industry's standard dummy text ever since the 1500s...</p>

  <div class="tile" style="left:21px;top:197px"><div class="photo" role="img" aria-label="Fish fillet topped with mango salsa" style="background:linear-gradient(160deg,#3a2a1a,#e0b060 50%,#f2efe8)"></div><div class="caption">Fried asorted food</div></div>
  <div class="tile" style="left:221px;top:197px"><div class="photo" role="img" aria-label="Plate of beef with beans and rice" style="background:linear-gradient(160deg,#efeeea,#8a6a4a 50%,#6b6a40)"></div><div class="caption">Fried asorted food</div></div>
  <div class="tile" style="left:420px;top:197px"><div class="photo" role="img" aria-label="Ceviche cup with lime and tortilla chips" style="background:linear-gradient(160deg,#a8401a,#c8d0a8 45%,#e8b040)"></div><div class="caption">Fried asorted food</div></div>
  <div class="tile" style="left:21px;top:399px"><div class="photo" role="img" aria-label="Braised pork with pickled onion and rice" style="background:linear-gradient(160deg,#e8e4dc,#c04060 35%,#5a2a14)"></div><div class="caption">Fried asorted food</div></div>
  <div class="tile" style="left:221px;top:399px"><div class="photo" role="img" aria-label="Grilled salmon on a wooden plank" style="background:linear-gradient(160deg,#302820,#e8e6e2 40%,#d08040)"></div><div class="caption">Fried asorted food</div></div>
  <div class="tile" style="left:420px;top:399px"><div class="photo" role="img" aria-label="Guacamole in a stone bowl with chips" style="background:linear-gradient(160deg,#c04030,#7aa040 45%,#3a3a3a)"></div><div class="caption">Fried asorted food</div></div>

  <div class="pager">
    <span><svg width="10" height="14" viewBox="0 0 10 14"><path d="M8 1 2 7l6 6" fill="none" stroke="#fff" stroke-width="1.5"/></svg></span>
    <span><svg width="10" height="14" viewBox="0 0 10 14"><path d="M2 1l6 6-6 6" fill="none" stroke="#fff" stroke-width="1.5"/></svg></span>
  </div>
</section>

<div class="abs footer">Home<span class="sep">/</span>Menu<span class="sep">/</span>Contact<span class="sep">/</span>Calender<span class="sep">/</span>Press<span class="sep">/</span>Gallery</div>
<div class="abs copy">© La Brisa Taqueria. 2014. All rights reserved.</div>
</body>
</html>
```